Sticker(s) for a brisk tomato road trip

We need a bumper sticker sz and style design with the word - brsktmt.
I envision the v with a red heart in it, a black background white lettering...but I'm open to other creative flow.
We have a custom Alberta lic plate with brsktmt for our 1977 ZK van on its way. Could also get fun with a copy of lic plate design.
Please include our website on it as well: brsktmt.ca
Thank you!!! :)))

```html
<!DOCTYPE html>
<html lang="en">
<head>
<meta charset="utf-8">
<title>Brisk Tomato Bumper Sticker</title>
<link rel="stylesheet" href="https://fonts.googleapis.com/css2?family=Bebas+Neue&family=Yellowtail&family=Space+Grotesk:wght@400&display=swap">
<style>
  :root {
    --page: #ffffff;
    --plate-bg: #dfe5e5;
    --plate-face: #e4e8e8;
    --plate-rim: #f3f5f5;
    --plate-rim-shadow: #c9cfcf;
    --navy: #0a0a55;
    --red: #ff0a0a;
    --bolt: #222526;
    --label: #222222;
  }
  html, body {
    margin: 0;
    padding: 0;
    width: 1200px;
    height: 900px;
    overflow: hidden;
    background: var(--page);
  }
  .canvas {
    position: relative;
    width: 1200px;
    height: 900px;
  }
  .size-label {
    position: absolute;
    left: 239px;
    top: 303px;
    margin: 0;
    font-family: "Space Grotesk", sans-serif;
    font-size: 17px;
    color: var(--label);
    letter-spacing: -0.5px;
  }
  .sticker {
    position: absolute;
    left: 240px;
    top: 342px;
    width: 720px;
    height: 216px;
    background: var(--plate-bg);
  }
  .plate-rim {
    position: absolute;
    left: 9px;
    top: 9px;
    width: 702px;
    height: 198px;
    box-sizing: border-box;
    border-radius: 16px;
    background: var(--plate-face);
    border: 2px solid var(--plate-rim);
    box-shadow: 0 0 0 1px var(--plate-rim-shadow), inset 0 0 0 1px var(--plate-rim-shadow);
  }
  .bolt {
    position: absolute;
    width: 13px;
    height: 13px;
    border-radius: 50%;
    background: var(--bolt);
  }
  .bolt.top-left { left: 78px; top: 21px; }
  .bolt.top-right { left: 628px; top: 21px; }
  .bolt.bottom-left { left: 78px; top: 181px; }
  .bolt.bottom-right { left: 628px; top: 181px; }
  .tagline {
    position: absolute;
    left: 0;
    width: 100%;
    top: 10px;
    margin: 0;
    text-align: center;
    font-family: "Yellowtail", cursive;
    font-size: 33px;
    font-weight: 400;
    color: var(--red);
  }
  .plate-number {
    position: absolute;
    left: 0;
    width: 100%;
    top: 52px;
    margin: 0;
    text-align: center;
    font-family: "Bebas Neue", sans-serif;
    font-size: 136px;
    line-height: 1;
    font-weight: 400;
    letter-spacing: 11px;
    padding-left: 11px;
    box-sizing: border-box;
    color: var(--navy);
    text-shadow: 1px 2px 0 #ffffff, 2px 3px 3px rgba(0,0,0,0.15);
  }
  .heart {
    position: absolute;
    top: 80px;
    width: 76px;
    height: 68px;
  }
  .heart.left { left: 47px; }
  .heart.right { left: 597px; }
  .heart path { fill: var(--red); }
  .website {
    position: absolute;
    left: 0;
    width: 100%;
    top: 174px;
    margin: 0;
    text-align: center;
    font-family: "Bebas Neue", sans-serif;
    font-size: 23px;
    letter-spacing: 1px;
    color: var(--red);
  }
</style>
</head>
<body>
  <main class="canvas">
    <p class="size-label">10 x 3</p>
    <section class="sticker">
      <div class="plate-rim"></div>
      <span class="bolt top-left"></span>
      <span class="bolt top-right"></span>
      <span class="bolt bottom-left"></span>
      <span class="bolt bottom-right"></span>

      <p class="tagline">Brisk Tomato</p>

      <svg class="heart left" viewBox="0 0 76 68" aria-hidden="true">
        <path d="M38 68 L6 36 A19 19 0 0 1 38 8 A19 19 0 0 1 70 36 Z"/>
      </svg>
      <h1 class="plate-number">BRSKTMT</h1>
      <svg class="heart right" viewBox="0 0 76 68" aria-hidden="true">
        <path d="M38 68 L6 36 A19 19 0 0 1 38 8 A19 19 0 0 1 70 36 Z"/>
      </svg>

      <p class="website">Visit brsktmt.ca</p>
    </section>
  </main>
</body>
</html>
```